Educational Agency in Abu Dhabi looking for an 8 pages website

We are looking for an 8 pages design for a website, we already have one but we need to refine it and it is www.korvalendi.ae - Please base it on logo colours (attached) I have uploaded our logo, website content logo colors to use it for the scheme.
We are looking for a smooth look and content added if possible, I also attached content and logo

Industry/Entity Type

Education

Coding

Coded - Design and coding required

Number of Pages Required

5+ page

```html
<!DOCTYPE html>
<html lang="en">
<head>
<meta charset="utf-8">
<title>Korvalendi – Educational Consulting</title>
<link href="https://fonts.googleapis.com/css2?family=Roboto:ital,wght@0,400;0,500;0,700;0,900;1,400&display=swap" rel="stylesheet">
<style>
:root{
  --navy:#1f2b5e;
  --navy-deep:#19224d;
  --ink:#1c1c1c;
  --body:#2b2b2b;
  --muted:#5a5a5a;
  --dark:#242222;
  --band:#e4e4e4;
  --white:#ffffff;
  --accent:#7b2b8f;
  --grey-btn:#d9d9d9;
}
*{box-sizing:border-box;margin:0;padding:0}
html,body{width:1200px;height:2782px;overflow:hidden;background:var(--white)}
body{font-family:"Roboto",Arial,sans-serif;color:var(--body)}
.page{position:relative;width:1200px;height:2782px;overflow:hidden}
.abs{position:absolute}

/* hero */
.hero{left:0;top:0;width:1200px;height:716px;overflow:hidden}
.hero-photo{position:absolute;inset:0;background:linear-gradient(115deg,#cfc9c1 0%,#e9e5de 35%,#d7cfc4 55%,#9ea590 75%,#3f6e4c 100%)}
.hero-shape{position:absolute;inset:0}
.brand-box{left:52px;top:0;width:172px;height:247px;background:var(--white);display:flex;flex-direction:column;align-items:center;justify-content:center;gap:10px}
.brand-mark{width:22px;height:22px;background:var(--navy)}
.brand-name{font-weight:700;font-size:24px;color:var(--navy);letter-spacing:1px}
.top-btn{top:18px;height:30px;border-radius:15px;font-size:12px;display:flex;align-items:center;justify-content:center}
.btn-apply{left:974px;width:95px;background:var(--accent);color:var(--white)}
.btn-contact{left:1076px;width:89px;background:#f2f2f2;color:var(--ink);border:1px solid #bbb}
.nav{left:316px;top:67px;width:884px;height:30px;background:rgba(25,25,25,.82);display:flex;justify-content:flex-end;align-items:center;padding-right:35px}
.nav a{color:var(--white);font-size:13.5px;font-weight:700;text-decoration:none;padding:0 10px;border-left:1px solid rgba(255,255,255,.6);line-height:14px}
.nav a:first-child{border-left:none}
.hero-title{left:54px;top:318px;font-weight:900;font-size:63px;line-height:76px;color:var(--white);text-shadow:0 0 2px #000,2px 2px 0 rgba(0,0,0,.6);letter-spacing:.5px}
.hero-sub{left:54px;top:468px;font-size:18px;font-weight:500;color:var(--ink);text-shadow:0 0 3px rgba(255,255,255,.8)}
.btn-reserve{left:54px;top:514px;width:326px;height:47px;background:var(--white);border-radius:8px;font-weight:700;font-size:18px;color:var(--ink);display:flex;align-items:center;justify-content:center;letter-spacing:.5px}

/* partner + news cards */
.card{top:645px;width:232px;height:349px;border-radius:10px;overflow:hidden;box-shadow:0 4px 14px rgba(0,0,0,.25)}
.card-head{height:70px;display:flex;align-items:center;justify-content:center;font-size:24px;font-weight:500}
.partners{left:658px;background:var(--navy)}
.partners .card-head{background:var(--white);color:var(--ink)}
.partner-list{list-style:none;padding:12px 30px 0 22px;position:relative}
.partner-list li{color:#e9ecff;font-size:12.5px;line-height:19.5px;padding-left:14px;position:relative}
.partner-list li::before{content:"";position:absolute;left:0;top:8px;width:4px;height:4px;border-radius:50%;background:#8e97c4}
.scroll-white{position:absolute;right:18px;top:94px;width:4px;height:70px;background:var(--white)}
.news{left:931px;background:var(--white)}
.news .card-head{background:var(--navy);color:var(--white)}
.news-body{padding:14px 26px 0 22px;position:relative}
.news-item{margin-bottom:16px}
.news-item h4{font-size:15px;font-weight:500;color:var(--ink);padding-left:12px;position:relative}
.news-item h4::before{content:"";position:absolute;left:0;top:7px;width:5px;height:5px;border-radius:50%;background:var(--ink)}
.news-item h4 span{color:var(--navy)}
.news-item p{font-size:10.5px;line-height:13px;color:var(--muted);text-align:justify;margin-top:5px}
.news-scroll{position:absolute;right:16px;top:88px;width:4px;height:240px;background:#e6e6e6}
.news-scroll::after{content:"";position:absolute;left:0;top:0;width:4px;height:70px;background:var(--navy)}

/* about */
.h2{font-size:46px;font-weight:500;color:var(--ink)}
.rule{width:95px;height:9px;background:var(--navy)}
.about-title{left:54px;top:768px}
.about-rule{left:54px;top:846px}
.about-text{left:54px;top:882px;width:546px;font-size:15px;line-height:18.5px;color:var(--body);text-align:justify;hyphens:auto}
.about-text p{margin-bottom:18px}
.about-wide{left:54px;top:1051px;font-size:15px;color:var(--body)}
.btn-app{left:54px;top:1111px;width:341px;height:65px;border-radius:8px;overflow:hidden;display:flex}
.btn-app .label{width:281px;background:var(--navy);color:var(--white);font-size:21px;font-weight:500;display:flex;align-items:center;justify-content:center}
.btn-app .go{flex:1;background:var(--grey-btn);display:flex;align-items:center;justify-content:center}

/* destinations */
.dest{left:0;top:1221px;width:1200px;height:556px;background:linear-gradient(135deg,#2f2e2e,#1f1e1e 60%,#2c2b2b)}
.dest-photo{position:absolute;left:0;top:0;width:408px;height:556px;background:linear-gradient(160deg,#7a5a3f 0%,#a99c8e 35%,#6f7f92 60%,#4a5c78 85%,#3a3f4b 100%)}
.dest-title{position:absolute;left:408px;width:792px;top:36px;text-align:center;font-size:46px;font-weight:500;color:var(--white)}
.dest-card{position:absolute;width:213px;height:111px;border:3px solid var(--white)}
.dest-card .flag{position:absolute;left:32px;top:-46px;width:70px;height:70px;border-radius:50%;box-shadow:0 2px 6px rgba(0,0,0,.5)}
.dest-card h3{position:absolute;left:12px;top:26px;font-size:23px;font-weight:400;color:var(--white);white-space:nowrap}
.dest-card p{position:absolute;left:12px;top:58px;width:170px;font-size:10px;line-height:12px;font-style:italic;color:#e5e5e5}
.dest-card .arrow{position:absolute;right:-16px;bottom:-16px;width:30px;height:30px;border-radius:50%;background:#cfcfcf;display:flex;align-items:center;justify-content:center}

/* why */
.why-title{left:54px;top:1826px}
.why-rule{left:54px;top:1905px}
.why-intro{left:54px;top:1940px;width:1100px;font-size:15px;line-height:20px;color:var(--body)}
.feature{width:360px}
.feature svg{position:absolute;left:0;top:0}
.feature h4{position:absolute;left:52px;top:0;width:300px;font-size:19px;font-weight:500;line-height:20px;color:var(--ink)}
.feature p{position:absolute;left:52px;width:256px;font-size:13px;line-height:16.5px;color:var(--muted);text-align:justify}

/* accreditation band */
.band{left:0;top:2356px;width:1200px;height:154px;background:var(--band)}

/* footer */
.foot-left{left:0;top:2510px;width:499px;height:272px;background:var(--white)}
.foot-right{left:499px;top:2510px;width:701px;height:272px;background:var(--dark)}
.foot-brand{left:74px;top:2560px;width:180px;display:flex;flex-direction:column;align-items:center;gap:10px}
.copyright{left:58px;top:2748px;font-size:12px;color:var(--ink)}
.foot-h{font-size:22px;font-weight:700}
.links-title{left:332px;top:2552px;color:var(--navy)}
.link-list{list-style:none;font-size:16px;line-height:25.6px}
.links-a{left:332px;top:2594px;color:var(--ink)}
.links-b{left:536px;top:2594px;color:var(--white)}
.contact-title{left:744px;top:2552px;color:var(--white)}
.contact{left:744px;top:2594px;font-size:16px;line-height:25.6px;color:var(--white)}
.social{left:1054px;top:2558px;display:flex;flex-direction:column;gap:22px}
.social span{display:block;width:32px;height:32px;border:2px solid var(--white);border-radius:5px}
.social-rule{left:1113px;top:2552px;width:3px;height:180px;background:var(--navy)}
.socialize{left:1141px;top:2700px;transform:rotate(-90deg);transform-origin:0 0;color:var(--white);font-size:20px;font-weight:700;letter-spacing:1px}
</style>
</head>
<body>
<div class="page">

  <section class="abs hero">
    <div class="hero-photo" role="img" aria-label="Photo of four smiling students gathered around a laptop"></div>
    <svg class="hero-shape" width="1200" height="716" viewBox="0 0 1200 716" aria-hidden="true">
      <polygon points="0,0 560,0 330,716 0,716" fill="#1f2b5e" opacity=".55"/>
      <polygon points="0,0 250,0 560,716 0,716" fill="#19224d" opacity=".85"/>
    </svg>
    <div class="abs brand-box">
      <span class="brand-mark"></span>
      <span class="brand-name">KORVALENDI</span>
    </div>
    <div class="abs top-btn btn-apply">Apply Now</div>
    <div class="abs top-btn btn-contact">Contact Us</div>
    <nav class="abs nav">
      <a>Aboutus</a><a>Why Study Abroad</a><a>Study Destinations</a><a>Our Sevices</a><a>Study English Language</a><a>Courses</a><a>Scholarship</a>
    </nav>
    <h1 class="abs hero-title">EXPERIENCED<br>COUNSELORS AVAILABLE</h1>
    <p class="abs hero-sub">To help you identify the best education plan for you!</p>
    <div class="abs btn-reserve">•&nbsp;&nbsp;RESERVE A CLASS&nbsp;&nbsp;•</div>
  </section>

  <aside class="abs card partners">
    <div class="card-head">OUR PARTNERS</div>
    <ul class="partner-list">
      <li>University of Ashmoor</li>
      <li>University of Kellbridge</li>
      <li>Danford City University</li>
      <li>University of Seabrook</li>
      <li>University of Wendleham</li>
      <li>University of East Marston</li>
      <li>University of Cranley</li>
      <li>University of Tynemoor</li>
      <li>ONTO Hollingford</li>
      <li>Glenmore Caledon<br>University</li>
      <li>Queen's University Larnwick</li>
    </ul>
    <span class="scroll-white"></span>
  </aside>

  <aside class="abs card news">
    <div class="card-head">NEWS &amp; UPDATES</div>
    <div class="news-body">
      <div class="news-item"><h4>News <span>#1</span></h4><p>We officially collaborate with over 300 domestic and international accredited educational institutions to ensure you get the best quality.</p></div>
      <div class="news-item"><h4>News <span>#2</span></h4><p>We officially collaborate with over 300 domestic and international accredited educational institutions to ensure you get the best quality.</p></div>
      <div class="news-item"><h4>News <span>#3</span></h4><p>We officially collaborate with over</p></div>
    </div>
    <span class="news-scroll"></span>
  </aside>

  <h2 class="abs h2 about-title">Who Are We?</h2>
  <div class="abs rule about-rule"></div>
  <div class="abs about-text">
    <p>KORVALENDI Abu Dhabi, one of the leading and fastest growing educational consulting company based in UAE officially recognized by Council of Higher Learning and Applied Research, Orvia Agency and QMS-4017.</p>
    <p>Korvalendi was established in 2015 with an aim to provide professional consultancy services for the recruitment of quality international students to educational institutions based in UK, USA, Canada, Australia, Malaysia, Germany, Europe, Middle East and many more.</p>
  </div>
  <p class="abs about-wide">Our counseling, services focus on student careers making sure that they are well placed in good and reputed institutions overseas.</p>
  <div class="abs btn-app">
    <div class="label">MAKE AN APPLICATION</div>
    <div class="go"><svg width="20" height="24" viewBox="0 0 20 24"><polyline points="5,3 15,12 5,21" fill="none" stroke="#7b2b8f" stroke-width="4"/></svg></div>
  </div>

  <section class="abs dest">
    <div class="dest-photo" role="img" aria-label="Photo of three students chatting on outdoor steps with a laptop"></div>
    <h2 class="dest-title">Study Destination</h2>

    <div class="dest-card" style="left:451px;top:185px">
      <span class="flag" role="img" aria-label="UK flag" style="background:radial-gradient(circle at 40% 35%,#e8e8ef,#c8102e 45%,#012169 80%)"></span>
      <h3>Study in UK</h3><p>Lorem ipsum dolor sit amet, consectetur adipiscing elit, sed do</p>
      <span class="arrow"><svg width="12" height="12" viewBox="0 0 12 12"><polyline points="4,2 8,6 4,10" fill="none" stroke="#333" stroke-width="2"/></svg></span>
    </div>
    <div class="dest-card" style="left:701px;top:185px">
      <span class="flag" role="img" aria-label="USA flag" style="background:radial-gradient(circle at 35% 35%,#3c4f8c,#f1f1f1 50%,#b22234 85%)"></span>
      <h3>Study in USA</h3><p>Lorem ipsum dolor sit amet, consectetur adipiscing elit, sed do</p>
      <span class="arrow"><svg width="12" height="12" viewBox="0 0 12 12"><polyline points="4,2 8,6 4,10" fill="none" stroke="#333" stroke-width="2"/></svg></span>
    </div>
    <div class="dest-card" style="left:952px;top:185px">
      <span class="flag" role="img" aria-label="Australia flag" style="background:radial-gradient(circle at 35% 35%,#c8102e,#2b3f8f 45%,#00247d 85%)"></span>
      <h3>Study in Australia</h3><p>Lorem ipsum dolor sit amet, consectetur adipiscing elit, sed do</p>
      <span class="arrow"><svg width="12" height="12" viewBox="0 0 12 12"><polyline points="4,2 8,6 4,10" fill="none" stroke="#333" stroke-width="2"/></svg></span>
    </div>
    <div class="dest-card" style="left:451px;top:374px">
      <span class="flag" role="img" aria-label="Germany flag" style="background:linear-gradient(#111 0 33%,#dd0000 33% 66%,#ffce00 66%)"></span>
      <h3>Study in Germany</h3><p>Lorem ipsum dolor sit amet, consectetur adipiscing elit, sed do</p>
      <span class="arrow"><svg width="12" height="12" viewBox="0 0 12 12"><polyline points="4,2 8,6 4,10" fill="none" stroke="#333" stroke-width="2"/></svg></span>
    </div>
    <div class="dest-card" style="left:701px;top:374px">
      <span class="flag" role="img" aria-label="China flag" style="background:radial-gradient(circle at 30% 30%,#ffde00 0 8%,#de2910 12%)"></span>
      <h3>Study in China</h3><p>Lorem ipsum dolor sit amet, consectetur adipiscing elit, sed do</p>
      <span class="arrow"><svg width="12" height="12" viewBox="0 0 12 12"><polyline points="4,2 8,6 4,10" fill="none" stroke="#333" stroke-width="2"/></svg></span>
    </div>
    <div class="dest-card" style="left:952px;top:374px">
      <span class="flag" role="img" aria-label="European Union flag" style="background:radial-gradient(circle at 40% 35%,#3a5fc0,#003399 70%)"></span>
      <h3>Study in Europe</h3><p>Lorem ipsum dolor sit amet, consectetur adipiscing elit, sed do</p>
      <span class="arrow"><svg width="12" height="12" viewBox="0 0 12 12"><polyline points="4,2 8,6 4,10" fill="none" stroke="#333" stroke-width="2"/></svg></span>
    </div>
    <svg class="abs" style="left:780px;top:518px" width="52" height="12" viewBox="0 0 52 12" aria-hidden="true">
      <circle cx="6" cy="6" r="4" fill="#8a8a8a"/><circle cx="26" cy="6" r="4" fill="#e6e6e6"/><circle cx="46" cy="6" r="4" fill="#8a8a8a"/>
    </svg>
  </section>

  <h2 class="abs h2 why-title">Why Korvalendi?</h2>
  <div class="abs rule why-rule"></div>
  <p class="abs why-intro">KORVALENDI Abu Dhabi, one of the leading and fastest growing educational consulting company based in UAE officially recognized by Council of Higher Learning and Applied Research, Orvia Agency and QMS-4017.</p>

  <div class="abs feature" style="left:57px;top:2018px">
    <svg width="40" height="40" viewBox="0 0 40 40" fill="none" stroke="#222" stroke-width="2"><rect x="4" y="12" width="32" height="26"/><polyline points="4,12 20,4 36,12"/><rect x="9" y="17" width="5" height="5"/><rect x="17.5" y="17" width="5" height="5"/><rect x="26" y="17" width="5" height="5"/><rect x="9" y="26" width="5" height="5"/><rect x="26" y="26" width="5" height="5"/><rect x="17" y="28" width="6" height="10"/></svg>
    <h4>Equiped Office</h4>
    <p style="top:30px">We have well-equipped office in ABU DHABI managed by an experienced team with counseling and good knowledge in overseas education.</p>
  </div>
  <div class="abs feature" style="left:454px;top:2018px">
    <svg width="40" height="40" viewBox="0 0 40 40" fill="none" stroke="#222" stroke-width="2"><rect x="10" y="3" width="24" height="32"/><rect x="5" y="8" width="24" height="30" fill="#fff"/><line x1="10" y1="15" x2="24" y2="15"/><line x1="10" y1="21" x2="24" y2="21"/><line x1="10" y1="27" x2="24" y2="27"/><line x1="10" y1="33" x2="20" y2="33"/></svg>
    <h4>Official tie up with Universities Institutions, and Schools</h4>
    <p style="top:48px">We have well-equipped office in ABU DHABI managed by an experienced team with counseling and good knowledge in overseas education.</p>
  </div>
  <div class="abs feature" style="left:851px;top:2018px">
    <svg width="40" height="40" viewBox="0 0 40 40" fill="none" stroke="#222" stroke-width="2"><circle cx="20" cy="20" r="17"/><circle cx="20" cy="15" r="6"/><path d="M9 32c2-7 7-9 11-9s9 2 11 9"/></svg>
    <h4>Experienced Counselors</h4>
    <p style="top:30px">We have well-equipped office in ABU DHABI managed by an experienced team with counseling and good knowledge in overseas education.</p>
  </div>
  <div class="abs feature" style="left:57px;top:2168px">
    <svg width="40" height="40" viewBox="0 0 40 40" fill="none" stroke="#222" stroke-width="2"><polygon points="20,3 25,15 38,15 27.5,23 31.5,36 20,28 8.5,36 12.5,23 2,15 15,15"/></svg>
    <h4>Quality of Counseling</h4>
    <p style="top:30px">We have well-equipped office in ABU DHABI managed by an experienced team with counseling and good knowledge in overseas education.</p>
  </div>
  <div class="abs feature" style="left:454px;top:2168px">
    <svg width="40" height="40" viewBox="0 0 40 40" fill="none" stroke="#222" stroke-width="2"><rect x="3" y="8" width="34" height="25" rx="2"/><circle cx="13" cy="18" r="4"/><path d="M7 28c1-4 4-5 6-5s5 1 6 5"/><line x1="23" y1="16" x2="33" y2="16"/><line x1="23" y1="21" x2="33" y2="21"/><line x1="23" y1="26" x2="30" y2="26"/></svg>
    <h4>Registration / License</h4>
    <p style="top:30px">We have well-equipped office in ABU DHABI managed by an experienced team with counseling and good knowledge in overseas education.</p>
  </div>
  <div class="abs feature" style="left:851px;top:2168px">
    <svg width="40" height="40" viewBox="0 0 40 40"><circle cx="20" cy="20" r="18" fill="#1c1c1c"/><path d="M10 12c4-2 7 1 9 4s-1 6-4 6-3 5-6 4-4-9 1-14zM24 9c4 1 9 4 10 10-3 0-5 3-7 6s-5 1-5-2 3-4 2-8-3-5 0-6z" fill="#fff"/></svg>
    <h4>Range of Countries</h4>
    <p style="top:30px">We have well-equipped office in ABU DHABI managed by an experienced team with counseling and good knowledge in overseas education.</p>
  </div>

  <section class="abs band" aria-label="Accreditation badges">
    <svg width="1200" height="154" viewBox="0 0 1200 154" aria-hidden="true">
      <circle cx="199" cy="64" r="36" fill="#b9b9b9"/>
      <rect x="144" y="110" width="110" height="6" fill="#b9b9b9"/>
      <rect x="160" y="122" width="78" height="5" fill="#c6c6c6"/>
      <circle cx="490" cy="60" r="34" fill="#a9a9a9"/>
      <rect x="435" y="106" width="110" height="6" fill="#a9a9a9"/>
      <rect x="455" y="118" width="70" height="5" fill="#b6b6b6"/>
      <rect x="648" y="42" width="210" height="72" rx="6" fill="#a3a3a3"/>
      <rect x="975" y="30" width="112" height="112" rx="10" fill="#9a9a9a"/>
    </svg>
  </section>

  <div class="abs foot-left"></div>
  <div class="abs foot-right"></div>
  <div class="abs foot-brand">
    <span class="brand-mark"></span>
    <span class="brand-name">KORVALENDI</span>
  </div>
  <p class="abs copyright">© Korvalendi Academic Service</p>

  <h3 class="abs foot-h links-title">QUICK LINKS</h3>
  <ul class="abs link-list links-a"><li>Home</li><li>Locations</li><li>Seasonal Menu</li><li>Story</li><li>Catering</li><li>Blog</li></ul>
  <ul class="abs link-list links-b"><li>Jobs</li><li>Gift Cards</li><li>Order Catering</li><li>Order Takeout</li><li>Contact</li><li>Press</li></ul>

  <h3 class="abs foot-h contact-title">CONTACT US</h3>
  <div class="abs contact">48 Larkfield Ave.<br>Brennan Bay, CA 90317<br>-<br>T: 555.214.3870<br>F: 555.214.3871</div>

  <div class="abs social" aria-label="Social links"><span></span><span></span><span></span><span></span></div>
  <div class="abs social-rule"></div>
  <div class="abs socialize">SOCIALIZE</div>

</div>
</body>
</html>
```